Emergency Management Consulting Flyer

Company name: Stone Harbor Emergency Management

I am looking for a postcard design for my emergency management consulting business. I'm looking for something that has some colors and is double sided, on side with the information on services provided and the other side with the contact information. For the main side I'm looking for the following:

How prepared are you?

Services Provided:
Healthcare Preparedness
EOC Support
Emergency Planning
Mitigation Planning
Business Continuity
Disaster Response
Training and Exercises
Project Management
And more

Affordable for small and large organizations
Stand-by contracts available

On the back side, I'm looking for Contact Us section.

Overall I'm looking for something a bit more modern and need to have at least one disaster photo. If you have questions please message me.

Target Market(s)

Government, Healthcare Facilities, Businesses

Industry/Entity Type

Consulting

Requirements
Must have
• Disaster Picture, modern looking
• For the main side I'm looking for the following:
• How prepared are you?
• Services Provided:
• Healthcare Preparedness
• EOC Support
• Emergency Planning
• Mitigation Planning
• Business Continuity
• Disaster Response
• Training and Exercises
• Project Management
• And more
• Affordable for small and large organizations
• Stand-by contracts available

```html
<!DOCTYPE html>
<html lang="en">
<head>
<meta charset="utf-8">
<title>Stone Harbor Emergency Management – Postcard</title>
<link rel="stylesheet" href="https://fonts.googleapis.com/css2?family=Comfortaa:wght@400;700&family=Oswald:wght@500;600&family=Open+Sans:ital,wght@0,300;0,400;1,700&display=swap">
<style>
  :root {
    --backdrop: #3d3d3f;
    --paper: #ffffff;
    --blue-light: #1b75bb;
    --blue-deep: #27398f;
    --navy: #2b3990;
    --orange-red: #e9522a;
    --orange: #f7941d;
    --text-dark: #2d2d2d;
    --text-grey: #444444;
    --panel-grey: #e6e7e8;
    --alert-red: #e3201b;
    --wood-light: #e9d3b6;
    --wood-dark: #9c7a5c;
  }
  * { box-sizing: border-box; margin: 0; padding: 0; }
  html, body { width: 801px; height: 1200px; overflow: hidden; }
  body { background: var(--backdrop); position: relative; font-family: "Open Sans", sans-serif; }

  .card {
    position: absolute; left: 42px; width: 711px; height: 550px;
    background: var(--paper); overflow: hidden;
    box-shadow: 4px 6px 10px rgba(0,0,0,.55);
  }
  .card--front { top: 44px; }
  .card--back { top: 614px; }

  /* Front */
  .headline {
    position: absolute; left: 0; top: 0; width: 100%; height: 94px;
    background: linear-gradient(90deg, var(--blue-light), var(--blue-deep));
    color: #fff; font-family: "Comfortaa", sans-serif; font-weight: 400;
    font-size: 50px; line-height: 94px; padding-left: 30px; letter-spacing: .5px;
    text-shadow: 1px 2px 3px rgba(0,0,0,.35);
  }
  .hero-photo {
    position: absolute; left: 306px; top: 94px; width: 405px; height: 456px;
    background: linear-gradient(100deg, #f3ede7 0%, #d9c9b6 45%, var(--wood-dark) 70%, #6b5a4c 100%);
  }
  .brand {
    position: absolute; display: flex; align-items: center; gap: 8px;
    font-family: "Comfortaa", sans-serif; font-weight: 700; color: var(--navy);
    text-transform: uppercase; line-height: 1.1;
  }
  .brand__dot { width: 44px; height: 44px; border-radius: 50%; background: var(--orange-red); flex: none; }
  .card--front .brand { left: 27px; top: 110px; font-size: 17px; }

  .services { position: absolute; left: 31px; top: 184px; }
  .services__title {
    font-family: "Comfortaa", sans-serif; font-weight: 400; font-size: 22px;
    color: var(--orange-red); margin-bottom: 10px;
  }
  .services__list { list-style: none; }
  .services__list li {
    font-family: "Comfortaa", sans-serif; font-size: 15px; color: var(--text-dark);
    height: 23.7px; line-height: 23.7px; padding-left: 25px; position: relative;
  }
  .services__list li::before {
    content: ""; position: absolute; left: 0; top: 5px; width: 14px; height: 14px; border-radius: 50%;
    background: radial-gradient(circle at 35% 35%, #ffffff 0%, #b8b8b8 45%, #5e5e5e 100%);
  }

  .bands { position: absolute; left: 0; top: 0; }
  .offer {
    position: absolute; left: 31px; top: 456px;
    font-family: "Oswald", sans-serif; font-weight: 600; font-size: 22px; line-height: 27px;
    color: #fff; text-shadow: 1px 1px 2px rgba(0,0,0,.35);
  }
  .call-front {
    position: absolute; left: 386px; top: 498px;
    font-family: "Oswald", sans-serif; font-weight: 600; font-size: 32px; line-height: 40px;
    color: #fff; letter-spacing: .5px; text-shadow: 1px 1px 2px rgba(0,0,0,.35);
  }

  /* Back */
  .domino-photo {
    position: absolute; left: 0; top: 0; width: 334px; height: 236px;
    background: linear-gradient(160deg, var(--wood-light) 0%, #f4ece2 45%, #2f3440 75%, #d8c2a3 100%);
  }
  .card--back .brand { left: 186px; top: 36px; font-size: 19px; }
  .mail-zones { position: absolute; left: 0; top: 0; }
  .mail-label {
    position: absolute; font-family: Arial, Helvetica, sans-serif; font-size: 19px;
    color: #111; text-align: center; line-height: 26px;
  }
  .contact { position: absolute; left: 0; width: 354px; text-align: center; }
  .contact__note {
    top: 246px; font-weight: 300; font-size: 22px; line-height: 30px; color: var(--text-grey);
  }
  .contact__phone {
    top: 354px; font-family: "Oswald", sans-serif; font-weight: 600; font-size: 35px;
    line-height: 44px; color: var(--navy);
  }
  .contact__address {
    top: 400px; font-style: italic; font-weight: 700; font-size: 16px;
    color: var(--alert-red); line-height: 22px;
  }
</style>
</head>
<body>

<section class="card card--front">
  <h1 class="headline">How prepared are you?</h1>
  <div class="hero-photo" role="img" aria-label="Photo of hands removing a block from a wooden stacking tower"></div>

  <div class="brand"><span class="brand__dot"></span><span>Stone Harbor<br>Emergency Management</span></div>

  <div class="services">
    <h2 class="services__title">Services Provided</h2>
    <ul class="services__list">
      <li>Healthcare Preparedness</li>
      <li>EOC Support</li>
      <li>Emergency Planning</li>
      <li>Mitigation Planning</li>
      <li>Business Continuity</li>
      <li>Disaster Response</li>
      <li>Training and Exercises</li>
      <li>Project Management</li>
      <li>And more</li>
    </ul>
  </div>

  <svg class="bands" width="711" height="550" viewBox="0 0 711 550" aria-hidden="true">
    <defs>
      <linearGradient id="band-orange" x1="0" x2="1" y1="0" y2="0">
        <stop offset="0" stop-color="var(--orange-red)"/>
        <stop offset="1" stop-color="var(--orange)"/>
      </linearGradient>
      <linearGradient id="band-blue" x1="0" x2="1" y1="0" y2="0">
        <stop offset="0" stop-color="var(--blue-light)"/>
        <stop offset="1" stop-color="var(--blue-deep)"/>
      </linearGradient>
    </defs>
    <polygon points="0,450 376,450 341,550 0,550" fill="url(#band-orange)"/>
    <polygon points="366,488 711,488 711,550 343,550" fill="url(#band-blue)"/>
  </svg>

  <p class="offer">Affordable for small and<br>large organizations<br>Stand-by contracts available</p>
  <p class="call-front">Call Us: 01555 20417</p>
</section>

<section class="card card--back">
  <div class="domino-photo" role="img" aria-label="Photo of a hand stopping a row of falling wooden dominoes"></div>

  <div class="brand"><span class="brand__dot"></span><span>Stone Harbor<br>Emergency Management</span></div>

  <svg class="mail-zones" width="711" height="550" viewBox="0 0 711 550" aria-hidden="true">
    <rect x="534" y="18" width="159" height="158" fill="var(--panel-grey)"/>
    <polygon points="345,176 693,176 693,532 90,532 90,453 345,453" fill="var(--panel-grey)"/>
  </svg>
  <p class="mail-label" style="left:534px; top:70px; width:159px;">Postage<br>Area</p>
  <p class="mail-label" style="left:345px; top:215px; width:348px;">Address Area</p>
  <p class="mail-label" style="left:90px; top:484px; width:603px;">Barcode Area</p>

  <p class="contact contact__note">Affordable for small<br>and large organizations<br>Stand-by contracts available</p>
  <p class="contact contact__phone">Call: 01555 20417</p>
  <p class="contact contact__address">Suite 12, Harborview, Eastshire</p>
</section>

</body>
</html>
```